Qorva - Web Design Rebrand for Talent Resourcing Company

I need a new brand for a customer based in Ireland.
The website currently: https://braddick.io/
Braddick repositioning themselves to be strategic talent resourcing and operational technology consultancy, Specialising in Life Sciences and Data Centres.
Essentially their USP:
They have lots of specialist manufacturing & automation resources that understand the Life Sciences Industry

Competitor websites:
https://vernhollow.com/ I really like the clarity on this site and the pink/yellow mix could be replaced with a green/blue mix for Braddick?
https://tulimark.com/ These are a big company so anything we could steal would be good 😊

They want:
• Fresh, sharp imagery
• Movement on the main page (Margot is obsessed with this lol) so may be video on some sections?
• The facility to upload CVs so similar to above.
• A page to show types of jobs available
• A page to show types of resource available from Braddick
• About us
• Sectors they operate in (includes Life Sciences, Food & Bev, Data Centres)

Target Market(s)

HR/Recruitment/Talent Acquisition/Operations Personnel in Life Sciences and Data Centres

Industry/Entity Type

Life Sciences and Data Centres

Number of Pages Required

1 page

Font styles to use
Sans Serif

Colors
0054AA
0677BA
7BADD7
CADEEF
E8F1F8
0094D4
00A9DD
6FCCEA
C7EBF8
E9F6FB
00AB8E
00BBA5
67D7C9
C6EFE9
E9F9F6

Requirements
Must have
• Brand Colour might be green/blue mix OR if another colour combo compelling
Nice to have
• Fresh, Sharp imagery. Movement on the main image (maybe partial video)

```html
<!DOCTYPE html>
<html lang="en">
<head>
<meta charset="utf-8">
<title>Braddick – Strategic Talent Resourcing</title>
<link rel="stylesheet" href="https://fonts.googleapis.com/css2?family=Outfit:wght@300;400;500;600;700;800&family=Mulish:wght@400;600;700;800&display=swap">
<style>
:root{
  --teal-deep:#0b5767;
  --teal-dark:#0d4f5e;
  --teal:#00BBA5;
  --green:#00AB8E;
  --blue:#0054AA;
  --blue-mid:#0677BA;
  --sky:#00A9DD;
  --sky-soft:#6FCCEA;
  --mist:#E9F6FB;
  --mint:#E9F9F6;
  --ink:#1a1a1a;
  --body:#2c2c2c;
  --white:#ffffff;
  --head:"Outfit",sans-serif;
  --text:"Mulish",sans-serif;
}
*{box-sizing:border-box;margin:0;padding:0}
html,body{width:1200px;height:3236px;overflow:hidden}
body{position:relative;background:var(--white);font-family:var(--text);color:var(--body)}
.abs{position:absolute}

/* header */
.site-header{position:absolute;top:0;left:0;width:1200px;height:106px;z-index:5}
.brand-block{position:absolute;left:0;top:0;width:360px;height:106px;background:var(--teal-deep);clip-path:polygon(0 0,100% 0,84% 100%,0 100%)}
.brand-name{position:absolute;left:150px;top:14px;font-family:var(--head);font-weight:700;font-size:52px;color:var(--white);letter-spacing:-0.5px}
.top-strip{position:absolute;left:400px;top:0;height:47px;display:flex;align-items:center;gap:200px;font-family:var(--text);font-size:14px;font-weight:600;color:var(--ink)}
.top-strip span{display:flex;align-items:center;gap:16px}
.nav-bar{position:absolute;left:330px;top:47px;width:870px;height:53px;background:linear-gradient(90deg,var(--teal-deep),var(--blue-mid) 55%,var(--sky) 100%);clip-path:polygon(3% 0,100% 0,100% 100%,0 100%)}
.nav-bar ul{list-style:none;display:flex;gap:34px;position:absolute;left:123px;top:17px;font-family:var(--text);font-size:14px;font-weight:600;color:var(--white)}

/* hero */
.hero{position:absolute;top:0;left:0;width:1200px;height:820px;overflow:hidden}
.hero-photo{position:absolute;inset:0;background:linear-gradient(135deg,#5d7f93 0%,#3f6a80 40%,#6d8fa1 70%,#4d7388 100%)}
.hero-tint{position:absolute;inset:0;background:rgba(20,70,100,0.35)}
.hero-text{position:absolute;top:265px;left:0;width:1200px;text-align:center;color:var(--white);font-family:var(--head)}
.hero-text .line1{font-weight:300;font-size:46px;letter-spacing:0.5px;line-height:56px}
.hero-text .line2{font-weight:700;font-size:48px;line-height:66px}
.outline{color:transparent;-webkit-text-stroke:2px currentColor}
.hero-text .line3{font-weight:700;font-size:48px;line-height:58px;-webkit-text-stroke:2px var(--white);color:transparent}
.hero-text .tagline{font-family:var(--text);font-weight:700;font-size:15px;margin-top:22px}
.btn-dark{display:inline-block;background:var(--teal-dark);color:var(--white);font-family:var(--text);font-weight:800;font-size:13px;letter-spacing:0.5px;padding:13px 32px;margin-top:24px}

/* about */
.about-title{position:absolute;left:125px;top:792px;font-family:var(--head);font-weight:700;font-size:50px;color:var(--ink);letter-spacing:0.5px}
.about-title .outline{-webkit-text-stroke:2px var(--blue-mid)}
.about-copy{position:absolute;left:125px;top:865px;width:520px;font-size:14px;line-height:21px;color:var(--body)}
.about-copy p{margin-bottom:21px}
.btn-outline{position:absolute;left:125px;top:1157px}
.about-photo{position:absolute;left:703px;top:583px;width:400px;height:714px;background:linear-gradient(160deg,#2b3f7a 0%,#5a6fb0 30%,#c7b8a8 60%,#8d7463 100%)}

/* team */
.team{position:absolute;left:0;top:1297px;width:1200px;height:540px;background:linear-gradient(100deg,var(--blue) 0%,var(--blue-mid) 45%,var(--green) 100%);clip-path:polygon(0 0,100% 0,100% 57%,83% 75%,15% 75%,0 100%);text-align:center;color:var(--white)}
.team h2{font-family:var(--head);font-size:48px;line-height:50px;margin-top:100px}
.team h2 .light{font-weight:300}
.team h2 .bold{font-weight:700}
.team h2 .outline{-webkit-text-stroke:2px var(--white);font-weight:700}
.team p{font-size:14px;line-height:22px;width:960px;margin:0 auto}
.team p.first{margin-top:30px}
.team p.second{margin-top:16px}

/* roles */
.roles-title{position:absolute;left:125px;top:1790px;font-family:var(--head);font-weight:700;font-size:50px;color:var(--ink)}
.role-card{position:absolute;width:302px;height:356px;background:var(--mist);border-radius:4px;overflow:hidden}
.role-photo{position:absolute;left:0;top:0;width:302px;height:158px}
.role-name{position:absolute;left:0;top:158px;width:302px;height:40px;padding:9px 0 0 48px;background:linear-gradient(180deg,rgba(233,246,251,0.7),var(--mist));font-family:var(--head);font-weight:600;font-size:18px;color:var(--ink);margin-top:-22px}
.role-copy{position:absolute;left:48px;top:190px;width:230px;font-size:12.5px;line-height:19px;color:var(--ink)}
.role-btn{position:absolute;left:48px;top:294px;height:38px;padding:12px 46px 0 16px;background:var(--teal-dark);color:var(--white);font-family:var(--text);font-weight:800;font-size:10.5px;clip-path:polygon(0 0,88% 0,100% 50%,88% 100%,0 100%)}

/* stats */
.stats{position:absolute;left:0;top:2770px;width:1200px;height:217px;background:var(--teal-deep);color:var(--white)}
.stat{position:absolute;top:50px;width:300px;text-align:center}
.stat b{display:block;font-family:var(--head);font-weight:600;font-size:62px;line-height:70px}
.stat span{font-size:13px}

/* footer */
.footer-brand{position:absolute;left:165px;top:3072px;font-family:var(--head);font-weight:700;font-size:58px;color:var(--teal-deep)}
.footer-rule{position:absolute;width:3px;background:var(--blue-mid);top:3030px;height:170px}
.footer-links{position:absolute;left:439px;top:3030px;list-style:none;font-size:14px;line-height:26px;color:var(--ink)}
.footer-contact{position:absolute;left:628px;top:3056px;font-size:14px;line-height:25px;color:var(--ink)}
.social{position:absolute;top:3090px;width:32px;height:32px;border-radius:50%;background:var(--blue-mid)}
</style>
</head>
<body>

<section class="hero">
  <div class="hero-photo" role="img" aria-label="Photo of young professionals collaborating over documents at a meeting table"></div>
  <div class="hero-tint"></div>
  <svg class="abs" style="left:0;top:0" width="1200" height="820" viewBox="0 0 1200 820">
    <polygon points="0,480 205,680 0,680" fill="#0b5767" opacity="0.85"/>
    <polygon points="0,680 703,680 703,583 1103,583 1103,600 1200,520 1200,820 0,820" fill="#ffffff"/>
  </svg>
  <div class="hero-text">
    <div class="line1">STRATEGIC TALENT RESOURCING AND</div>
    <div class="line2">OPERATIONAL TECHNOLOGY</div>
    <div class="line3">EXPERTS</div>
    <div class="tagline">Specialising in Life Sciences and Data Centres.</div>
    <div class="btn-dark">CONTACT US</div>
  </div>
</section>

<header class="site-header">
  <div class="brand-block"></div>
  <div class="brand-name">Braddick</div>
  <div class="top-strip">
    <span>
      <svg width="18" height="18" viewBox="0 0 24 24"><path d="M6.6 10.8a15 15 0 0 0 6.6 6.6l2.2-2.2a1 1 0 0 1 1-.25 11.4 11.4 0 0 0 3.6.57 1 1 0 0 1 1 1V20a1 1 0 0 1-1 1A17 17 0 0 1 3 4a1 1 0 0 1 1-1h3.5a1 1 0 0 1 1 1c0 1.25.2 2.45.57 3.6a1 1 0 0 1-.25 1z" fill="#0677BA"/></svg>
      (555) 01-48270
    </span>
    <span>
      <svg width="20" height="15" viewBox="0 0 20 15"><rect x="0" y="0" width="20" height="15" rx="1.5" fill="#0677BA"/><path d="M1 1.5 10 8.5 19 1.5" stroke="#fff" stroke-width="1.6" fill="none"/></svg>
      hello@braddickmail.com
    </span>
  </div>
  <nav class="nav-bar">
    <ul>
      <li>Home</li><li>About Us</li><li>Capabilities</li><li>Our Clients</li><li>Join Our Team</li><li>Contact</li>
    </ul>
  </nav>
</header>

<section class="about">
  <h2 class="about-title">ABOUT <span class="outline">BRADDICK</span></h2>
  <div class="about-copy">
    <p>Braddick is proud to be providing top-tier resources to the life sciences sector, specialising in delivering high-quality talent and solutions that enhance the capabilities and operational excellence of our customers.</p>
    <p>Our operational technology expertise and talent pool has evolved over the past decade with successful project delivers for numerous life sciences organisations, so we are uniquely positioned to understand and meet your requirements.</p>
    <p>We are focused on matching the dynamic needs of life sciences firms with skilled professionals, thereby driving innovation and growth in this critical sector across Ireland.</p>
  </div>
  <svg class="btn-outline" width="175" height="42" viewBox="0 0 175 42">
    <polygon points="1,1 150,1 173,21 150,41 1,41" fill="#fff" stroke="#0b5767" stroke-width="1.5"/>
    <text x="36" y="26" font-family="Mulish,sans-serif" font-weight="800" font-size="12" fill="#1a1a1a">READ MORE</text>
  </svg>
  <div class="about-photo" role="img" aria-label="Photo of a team gathered around a laptop under a glowing network graphic"></div>
</section>

<section class="team">
  <h2><span class="light">MEAT </span><span class="bold">BRADDICK</span><br><span class="outline">TEAM</span></h2>
  <p class="first">Braddick employees have a variety of skills and experience, but they all are professional, experienced in their field and enjoy the variety of working at different client sites over time.</p>
  <p class="second">They get a feeling of success seeing a project through to completion, and are always willing to go the extra mile for our clients.</p>
</section>

<h2 class="roles-title">FEATURED ROLES:</h2>

<article class="role-card" style="left:125px;top:1895px">
  <div class="role-photo" role="img" aria-label="Photo of an engineer in a hard hat beside automated machinery" style="background:linear-gradient(135deg,#3d4a55,#8a96a0 60%,#c9ced2)"></div>
  <div class="role-name">Automation &amp; CSV</div>
  <div class="role-copy">Lorem Ipsum is simply dummy text of the printing and typesetting industry. Lorem Ipsum has been the industry's standard dummy text ever since the 1500s,</div>
  <div class="role-btn">EXPLORE AUTOMATION &amp; CSV JOBS</div>
</article>
<article class="role-card" style="left:447px;top:1895px">
  <div class="role-photo" role="img" aria-label="Photo of a scientist in goggles holding a sample dish" style="background:linear-gradient(135deg,#1f4d63,#5fa9bd 55%,#d7e8ee)"></div>
  <div class="role-name">Bioprocess</div>
  <div class="role-copy">Lorem Ipsum is simply dummy text of the printing and typesetting industry. Lorem Ipsum has been the industry's standard dummy text ever since the 1500s,</div>
  <div class="role-btn">EXPLORE BIOPROCESS JOBS</div>
</article>
<article class="role-card" style="left:769px;top:1895px">
  <div class="role-photo" role="img" aria-label="Photo of technicians in hard hats commissioning equipment" style="background:linear-gradient(135deg,#2d3545,#6a6f7c 50%,#d6a83a)"></div>
  <div class="role-name">Commissioning &amp; Validation</div>
  <div class="role-copy">Lorem Ipsum is simply dummy text of the printing and typesetting industry. Lorem Ipsum has been the industry's standard dummy text ever since the 1500s,</div>
  <div class="role-btn">EXPLORE C&amp;V JOBS</div>
</article>

<article class="role-card" style="left:125px;top:2305px">
  <div class="role-photo" role="img" aria-label="Photo of engineers in hard hats reviewing plans on site" style="background:linear-gradient(135deg,#b89a7a,#d8c7b3 50%,#8a7360)"></div>
  <div class="role-name">Engineering</div>
  <div class="role-copy">Lorem Ipsum is simply dummy text of the printing and typesetting industry. Lorem Ipsum has been the industry's standard dummy text ever since the 1500s,</div>
  <div class="role-btn">EXPLORE ENGINEERING JOBS</div>
</article>
<article class="role-card" style="left:447px;top:2305px">
  <div class="role-photo" role="img" aria-label="Photo of a project manager presenting to a team" style="background:linear-gradient(135deg,#2e2a33,#6b5c58 50%,#a88f7c)"></div>
  <div class="role-name">Project Management</div>
  <div class="role-copy">Lorem Ipsum is simply dummy text of the printing and typesetting industry. Lorem Ipsum has been the industry's standard dummy text ever since the 1500s,</div>
  <div class="role-btn">EXPLORE MANAGEMENT JOBS</div>
</article>
<article class="role-card" style="left:769px;top:2305px">
  <div class="role-photo" role="img" aria-label="Photo of a laboratory analyst working at a microscope" style="background:linear-gradient(135deg,#1d5f80,#59a6c9 55%,#cfe6f1)"></div>
  <div class="role-name">QC &amp; Laboratory</div>
  <div class="role-copy">Lorem Ipsum is simply dummy text of the printing and typesetting industry. Lorem Ipsum has been the industry's standard dummy text ever since the 1500s,</div>
  <div class="role-btn">EXPLORE QC &amp; LAB JOBS</div>
</article>

<section class="stats">
  <div class="stat" style="left:120px"><b>50+</b><span>Number skilled automation<br>engineers</span></div>
  <div class="stat" style="left:447px"><b>25+</b><span>Customers currently using<br>Braddick</span></div>
  <div class="stat" style="left:775px"><b>99%</b><span>Customer retention</span></div>
</section>

<footer>
  <div class="footer-brand">Braddick</div>
  <div class="footer-rule" style="left:408px"></div>
  <ul class="footer-links">
    <li>Home</li><li>About Us</li><li>Capabilities</li><li>Our Clients</li><li>Join Our Team</li><li>Contact</li>
  </ul>
  <div class="footer-rule" style="left:583px"></div>
  <div class="footer-contact">
    hello@braddickmail.com<br>
    (555) 01-48270<br>
    Unit 4b, Harrow Business Park,<br>
    Kilmore, Dublin 22.
  </div>
  <div class="footer-rule" style="left:855px"></div>
  <div class="social" style="left:900px"></div>
  <div class="social" style="left:950px"></div>
  <div class="social" style="left:1000px;background:var(--ink)"></div>
</footer>

</body>
</html>
```